Dorral Fitness fitness and wellness for 50+ and youth

We are a fitness company that caters to 50+ wellness and youth conditioning. Our motto is "We make fitness fun". We offer online wellness programs that include bootcamp style workouts as well as nutrition information/guidance. We would like a design that integrates our logo as well as bring attention to the FUN aspect of being healthy.

Target Market(s)

50+ and parents of teens & tweens

Industry/Entity Type

Fitness

Requirements
Must have
• Topic boxes
Nice to have
• Semi transparent grey or black header with logo integrated

```html
<!DOCTYPE html>
<html lang="en">
<head>
<meta charset="utf-8">
<title>Dorral Fitness</title>
<link rel="stylesheet" href="https://fonts.googleapis.com/css2?family=Lato:wght@400;700;900&family=Open+Sans:wght@400;600;700&display=swap">
<style>
:root{
  --green:#3dbb1f;
  --green-dark:#2a8e12;
  --black:#0d0d0d;
  --ink:#2b2b2b;
  --grey:#6b6b6b;
  --light:#f1f1f1;
  --card:#e4e4e4;
  --white:#ffffff;
}
*{box-sizing:border-box;margin:0;padding:0}
html,body{width:1200px;height:2204px;overflow:hidden}
body{position:relative;background:var(--white);font-family:"Open Sans",Arial,sans-serif;color:var(--ink)}
.abs{position:absolute}

/* header */
.site-header{left:0;top:0;width:1200px;height:140px;background:linear-gradient(#1b1b1b,#050505)}
.brand{left:128px;top:50px;display:flex;align-items:center;gap:14px;font-family:"Lato",sans-serif;font-weight:900;font-size:34px;color:var(--white);letter-spacing:1px}
.brand .mark{width:30px;height:30px;background:var(--green)}
.phone-tab{right:0;top:0;width:220px;height:48px;background:var(--green);border-bottom-left-radius:20px;display:flex;align-items:center;justify-content:center;gap:10px;color:var(--white);font-family:"Lato",sans-serif;font-weight:700;font-size:20px}
.badge{right:20px;width:188px;height:32px;background:var(--white);border-radius:4px;display:flex;align-items:center;gap:8px;padding-left:10px;font-size:13px;font-weight:700;color:var(--ink)}
.badge i{width:16px;height:16px;border-radius:50%;background:var(--grey);display:block}
.badge.social{top:56px}
.badge.appointment{top:100px}
.badge.appointment i{background:var(--green)}

/* nav */
.main-nav{left:0;top:140px;width:1200px;height:40px;background:linear-gradient(var(--green),var(--green-dark));display:flex;padding-left:128px}
.main-nav a{display:block;height:40px;line-height:40px;width:136px;text-align:center;color:var(--white);font-family:"Lato",sans-serif;font-size:15px;font-weight:700;text-decoration:none}
.main-nav a.active{background:#1e1e1e}

/* hero */
.hero{left:0;top:180px;width:1200px;height:480px;background:linear-gradient(100deg,#c9cdd0 0%,#a9aeb2 35%,#5d6266 65%,#3a3d40 100%)}
.hero-title{left:152px;top:522px;font-family:"Lato",sans-serif;font-size:38px;color:var(--white);font-weight:400}
.hero-dots{left:156px;top:578px;display:flex;gap:8px}
.hero-dots span{width:11px;height:11px;border-radius:50%;background:#bbb}
.hero-dots span:first-child{background:var(--white)}

/* topic boxes */
.topic{top:720px;width:224px;height:420px;background:linear-gradient(#eeeeee,#d2d2d2);border-radius:10px;box-shadow:0 10px 12px -6px rgba(0,0,0,.35);overflow:hidden;text-align:center}
.topic .photo{height:120px}
.topic .icon{width:84px;height:84px;border-radius:50%;background:linear-gradient(#999,#666);border:5px solid var(--white);margin:-36px auto 0;position:relative;display:flex;align-items:center;justify-content:center}
.topic .icon span{width:34px;height:34px;border-radius:50%;border:5px solid var(--white)}
.topic.featured .icon{background:linear-gradient(var(--green),var(--green-dark))}
.topic h3{font-family:"Lato",sans-serif;font-size:15px;font-weight:900;text-transform:uppercase;margin-top:24px;color:var(--ink)}
.topic p{font-size:12px;line-height:17px;color:var(--grey);padding:10px 22px 0}
.topic .more{display:inline-block;margin-top:36px;width:96px;height:28px;line-height:28px;border-radius:14px;background:#333;color:var(--white);font-size:12px;font-weight:700}
.topic.featured .more{background:var(--green)}

/* why choose us */
.section-title{font-family:"Lato",sans-serif;font-size:26px;font-weight:900;color:var(--ink);text-transform:uppercase}
.section-title em{font-style:normal;color:var(--green)}
.why{left:128px;top:1168px;width:520px}
.why p{font-size:12px;line-height:18px;color:var(--grey);margin-top:12px}
.why ul{list-style:none;margin-top:14px}
.why li{font-size:12px;line-height:24px;color:var(--grey);display:flex;align-items:center;gap:10px}
.why li svg{flex:none}
.video{left:688px;top:1168px;width:392px}
.video .player{margin-top:14px;height:220px;position:relative;background:linear-gradient(180deg,#8fa2b4,#c9c9bd 55%,#8f8a7c)}
.video .controls{position:absolute;left:0;bottom:0;width:100%;height:26px;background:rgba(0,0,0,.8);display:flex;align-items:center;gap:10px;padding:0 10px}
.video .bar{flex:1;height:5px;background:#555;position:relative}
.video .bar span{position:absolute;left:0;top:0;width:35%;height:5px;background:#d22}

/* services pills */
.service{top:1556px;height:64px;border-radius:32px;background:linear-gradient(#4a4a4a,#1c1c1c);display:flex;align-items:center;gap:18px;padding-left:6px;padding-right:28px;color:var(--white);font-family:"Lato",sans-serif;font-weight:700;font-size:16px;box-shadow:0 4px 6px rgba(0,0,0,.3)}
.service i{width:52px;height:52px;border-radius:50%;background:linear-gradient(var(--green),var(--green-dark));display:block;border:3px solid var(--white)}

/* gallery */
.gallery-title{left:0;top:1720px;width:1200px;text-align:center}
.gallery-title::before,.gallery-title::after{content:"";display:inline-block;width:300px;height:1px;background:#ccc;vertical-align:middle;margin:0 20px}
.shot{top:1784px;width:160px;height:136px;border:4px solid var(--white);box-shadow:0 2px 6px rgba(0,0,0,.35)}
.arrow{top:1836px;width:32px;height:32px;border-radius:50%;background:#444;display:flex;align-items:center;justify-content:center}

/* footer */
.site-footer{left:0;top:1960px;width:1200px;height:204px;background:var(--black);color:#cfcfcf}
.footer-col{top:1980px;font-size:12px;line-height:24px}
.footer-col h4{font-family:"Lato",sans-serif;font-size:15px;font-weight:700;color:var(--white);margin-bottom:8px;border-bottom:1px solid #333;padding-bottom:6px;width:200px}
.footer-col .row{display:flex;gap:10px;align-items:flex-start}
.footer-col .row i{width:14px;height:14px;border-radius:50%;background:#666;display:block;margin-top:5px;flex:none}
.footer-brand{left:900px;top:2040px;font-family:"Lato",sans-serif;font-weight:900;font-size:24px;color:#3a3a3a}
.bottom-bar{left:0;top:2164px;width:1200px;height:40px;background:linear-gradient(var(--green),var(--green-dark));display:flex;align-items:center;justify-content:space-between;padding:0 40px 0 24px;color:var(--white);font-size:12px}
.socials{display:flex;gap:8px}
.socials span{width:24px;height:24px;border-radius:50%;background:var(--white);display:block}
</style>
</head>
<body>

<header class="site-header abs">
</header>
<div class="brand abs"><span class="mark"></span>DORRAL FITNESS</div>
<div class="phone-tab abs">
  <svg width="18" height="18" viewBox="0 0 24 24"><path fill="#fff" d="M6.6 10.8a15 15 0 006.6 6.6l2.2-2.2a1 1 0 011-.25 11.4 11.4 0 003.6.57 1 1 0 011 1V20a1 1 0 01-1 1A17 17 0 013 4a1 1 0 011-1h3.5a1 1 0 011 1c0 1.25.2 2.45.57 3.57a1 1 0 01-.25 1z"/></svg>
  123 456 7890
</div>
<div class="badge social abs"><i></i>Like Us &amp; Follow Us</div>
<div class="badge appointment abs"><i></i>Get Appointment</div>

<nav class="main-nav abs">
  <a class="active">HOME</a><a>BLOG</a><a>ARCHIVES</a><a>CONTACT US</a><a>LINKS</a>
</nav>

<div class="hero abs" role="img" aria-label="Close-up photo of a hand lifting a dumbbell in a gym"></div>
<div class="hero-title abs">We Make Fitness Fun</div>
<div class="hero-dots abs"><span></span><span></span><span></span></div>

<article class="topic featured abs" style="left:128px">
  <div class="photo" role="img" aria-label="Photo of seniors exercising in a class" style="background:linear-gradient(#d7d2c7,#a9a294)"></div>
  <div class="icon"><span></span></div>
  <h3>Adult &amp; Senior Fitness</h3>
  <p>Lorem ipsum dolor sit amet, consectetuer adipiscing elit sed</p>
  <span class="more">READ MORE</span>
</article>
<article class="topic abs" style="left:372px">
  <div class="photo" role="img" aria-label="Photo of young people in a fitness class" style="background:linear-gradient(#c7b9a8,#8d7d6c)"></div>
  <div class="icon"><span></span></div>
  <h3>Youth Fitness</h3>
  <p>Lorem ipsum dolor sit amet, consectetuer adipiscing elit sed</p>
  <span class="more">READ MORE</span>
</article>
<article class="topic abs" style="left:616px">
  <div class="photo" role="img" aria-label="Photo of a laptop on a desk for online training" style="background:linear-gradient(#e9ecef,#aab3bb)"></div>
  <div class="icon"><span></span></div>
  <h3>Online Training Programs</h3>
  <p>Lorem ipsum dolor sit amet, consectetuer adipiscing elit sed</p>
  <span class="more">READ MORE</span>
</article>
<article class="topic abs" style="left:860px">
  <div class="photo" role="img" aria-label="Photo of a woman stretching outdoors in sunlight" style="background:linear-gradient(#f3d27a,#c99a3c)"></div>
  <div class="icon"><span></span></div>
  <h3>Wellness</h3>
  <p>Lorem ipsum dolor sit amet, consectetuer adipiscing elit sed</p>
  <span class="more">READ MORE</span>
</article>

<section class="why abs">
  <h2 class="section-title"><em>Why</em> Choose Us</h2>
  <p>Lorem ipsum dolor sit amet, consectetuer adipiscing elit, sed diam nonummy nibh euismod tincidunt ut laoreet dolore magna aliquam erat volutpat. Ut wisi enim ad minim veniam, quis nostrud exerci tation ullamcorper suscipit lobortis nisl ut aliquip.</p>
  <ul>
    <li><svg width="14" height="14" viewBox="0 0 14 14"><circle cx="7" cy="7" r="7" fill="#3dbb1f"/><path d="M3.5 7l2.5 2.5 4.5-5" stroke="#fff" stroke-width="2" fill="none"/></svg>Lorem ipsum dolor sit amet, consectetuer adipiscing elit</li>
    <li><svg width="14" height="14" viewBox="0 0 14 14"><circle cx="7" cy="7" r="7" fill="#3dbb1f"/><path d="M3.5 7l2.5 2.5 4.5-5" stroke="#fff" stroke-width="2" fill="none"/></svg>Sed diam nonummy nibh euismod tincidunt ut laoreet</li>
    <li><svg width="14" height="14" viewBox="0 0 14 14"><circle cx="7" cy="7" r="7" fill="#3dbb1f"/><path d="M3.5 7l2.5 2.5 4.5-5" stroke="#fff" stroke-width="2" fill="none"/></svg>Tincidunt ut laoreet dolore magna aliquam erat volutpat</li>
    <li><svg width="14" height="14" viewBox="0 0 14 14"><circle cx="7" cy="7" r="7" fill="#3dbb1f"/><path d="M3.5 7l2.5 2.5 4.5-5" stroke="#fff" stroke-width="2" fill="none"/></svg>Ut wisi enim ad minim veniam quis nostrud exerci</li>
    <li><svg width="14" height="14" viewBox="0 0 14 14"><circle cx="7" cy="7" r="7" fill="#3dbb1f"/><path d="M3.5 7l2.5 2.5 4.5-5" stroke="#fff" stroke-width="2" fill="none"/></svg>Tation ullamcorper suscipit lobortis nisl ut aliquip</li>
    <li><svg width="14" height="14" viewBox="0 0 14 14"><circle cx="7" cy="7" r="7" fill="#3dbb1f"/><path d="M3.5 7l2.5 2.5 4.5-5" stroke="#fff" stroke-width="2" fill="none"/></svg>Duis autem vel eum iriure dolor in hendrerit vulputate</li>
    <li><svg width="14" height="14" viewBox="0 0 14 14"><circle cx="7" cy="7" r="7" fill="#3dbb1f"/><path d="M3.5 7l2.5 2.5 4.5-5" stroke="#fff" stroke-width="2" fill="none"/></svg>Velit esse molestie consequat vel illum dolore eu</li>
    <li><svg width="14" height="14" viewBox="0 0 14 14"><circle cx="7" cy="7" r="7" fill="#3dbb1f"/><path d="M3.5 7l2.5 2.5 4.5-5" stroke="#fff" stroke-width="2" fill="none"/></svg>Feugiat nulla facilisis at vero eros et accumsan</li>
  </ul>
</section>

<section class="video abs">
  <h2 class="section-title">Video <em>Tips</em></h2>
  <div class="player" role="img" aria-label="Video still of a woman doing a lunge outdoors">
    <div class="controls">
      <svg width="12" height="12" viewBox="0 0 12 12"><path d="M2 1l9 5-9 5z" fill="#fff"/></svg>
      <div class="bar"><span></span></div>
      <svg width="14" height="12" viewBox="0 0 14 12"><path d="M1 4h3l4-3v10L4 8H1z" fill="#fff"/></svg>
    </div>
  </div>
</section>

<div class="service abs" style="left:128px"><i></i>Free Consultation</div>
<div class="service abs" style="left:436px"><i></i>Nutrition Guidance</div>
<div class="service abs" style="left:760px"><i></i>Get A Personal Trainer</div>

<h2 class="gallery-title section-title abs">View <em>Gallery</em></h2>
<div class="arrow abs" style="left:128px"><svg width="12" height="12" viewBox="0 0 12 12"><path d="M8 1L3 6l5 5" stroke="#fff" stroke-width="2" fill="none"/></svg></div>
<div class="shot abs" style="left:176px;background:linear-gradient(#b7c4cf,#6d7d89)" role="img" aria-label="Gallery photo of a group workout"></div>
<div class="shot abs" style="left:348px;background:linear-gradient(#d6cfc2,#918673)" role="img" aria-label="Gallery photo of a trainer with a client"></div>
<div class="shot abs" style="left:520px;background:linear-gradient(#e3e3e3,#9b9b9b)" role="img" aria-label="Gallery photo of seniors stretching"></div>
<div class="shot abs" style="left:692px;background:linear-gradient(#c9d7e3,#7f93a5)" role="img" aria-label="Gallery photo of youth playing sports"></div>
<div class="shot abs" style="left:864px;background:linear-gradient(#d8c8b0,#8e7656)" role="img" aria-label="Gallery photo of a couple jogging"></div>
<div class="arrow abs" style="left:1040px"><svg width="12" height="12" viewBox="0 0 12 12"><path d="M4 1l5 5-5 5" stroke="#fff" stroke-width="2" fill="none"/></svg></div>

<footer class="site-footer abs"></footer>
<div class="footer-col abs" style="left:128px">
  <h4>Quick Links</h4>
  <div>› Home</div><div>› Blogs</div><div>› Archives</div><div>› Contact Us</div><div>› Links</div>
</div>
<div class="footer-col abs" style="left:376px">
  <h4>Opening Hours</h4>
  <div class="row"><i></i><div>Monday to Saturday<br>8:00 AM To 9:00 PM</div></div>
  <div class="row" style="margin-top:8px"><i></i><div>Sunday<br>Closed</div></div>
</div>
<div class="footer-col abs" style="left:632px">
  <h4>Contact Us</h4>
  <div class="row"><i></i><div><strong style="color:#fff">Larkfield Avenue</strong><br>Lorem ipsum dolor sit amet</div></div>
  <div class="row"><i></i><div>+0123 456 789</div></div>
  <div class="row"><i></i><div>info@dorralfitness.com</div></div>
</div>
<div class="footer-brand abs">DORRAL FITNESS</div>
<div class="bottom-bar abs">
  <span>© 2015 Dorral Fitness. All Rights Reserved.</span>
  <div class="socials"><span></span><span></span><span></span></div>
</div>

</body>
</html>
```